Bref créative
BRISK FIELD Stationery
Stationery for BRISKFIELD web site
Professional
Tomas Kerbrune
7 Rue Montaleur, Res. Les Pins
Hendaye
info@briskfield-exemple.com
www.briskfield-exemple.com

```html
<!DOCTYPE html>
<html lang="en">
<head>
<meta charset="utf-8">
<title>BRISK FIELD Stationery</title>
<link href="https://fonts.googleapis.com/css2?family=Exo+2:wght@400;600;700&display=swap" rel="stylesheet">
<style>
:root{
  --board:#2e2e2f;
  --ink:#161617;
  --paper:#f4f4f4;
  --paper-edge:#dcdcdc;
  --accent:#d8372a;
  --accent-soft:#f08a3a;
  --muted:#9a9a9a;
  --label:#cfcfcf;
  --faint:#e6e6e6;
}
*{box-sizing:border-box;margin:0;padding:0}
html,body{width:1200px;height:600px;overflow:hidden}
body{background:var(--board);font-family:"Exo 2",sans-serif;position:relative}
.piece{position:absolute}
.label{position:absolute;color:var(--label);font-size:8px;letter-spacing:.5px;text-transform:uppercase;white-space:nowrap}
.brand{display:flex;flex-direction:column;align-items:center;gap:4px}
.brand-dot{width:18px;height:18px;border-radius:50%;background:var(--accent)}
.brand-name{color:#fff;font-weight:700;letter-spacing:1px;font-size:14px}
.rule{height:2px;background:linear-gradient(90deg,var(--accent),var(--accent-soft),var(--accent))}

/* business cards */
.card{left:24px;width:163px;height:91px;background:var(--ink);border:1px solid #444;padding:10px 12px}
.card-front{top:264px}
.card-back{top:389px;display:flex;flex-direction:column;align-items:center;justify-content:center}
.card .brand{align-items:flex-start;flex-direction:row;gap:5px;align-items:center}
.card .brand-dot{width:12px;height:12px}
.card .brand-name{font-size:12px}
.card-back .brand{flex-direction:column}
.card-person{margin-top:8px;color:var(--accent);font-size:6px;font-weight:600}
.card-role{color:var(--muted);font-size:5px}
.card-contact{margin-top:8px;color:var(--muted);font-size:4.5px}
.card-back .card-contact{margin-top:6px}

/* letterhead */
.letterhead{left:257px;top:48px;width:350px;height:523px;background:var(--paper);box-shadow:0 2px 6px rgba(0,0,0,.5)}
.letterhead-head{height:89px;background:var(--ink);display:flex;align-items:center;justify-content:center}
.watermark{position:absolute;left:105px;top:270px;width:140px;height:140px;border-radius:50%;border:10px solid var(--faint);display:flex;align-items:center;justify-content:center}
.watermark span{color:var(--faint);font-weight:700;font-size:18px;letter-spacing:1px}
.letterhead-foot{position:absolute;left:0;right:0;bottom:0;padding:0 14px 12px}
.foot-text{margin-top:7px;color:#555;font-size:5.5px;display:flex;gap:10px}
.foot-text i{color:var(--accent);font-style:normal}

/* envelopes */
.envelope{left:700px;width:452px;background:var(--paper);box-shadow:0 2px 6px rgba(0,0,0,.5);overflow:hidden}
.env-one{top:72px;height:211px}
.env-one svg{position:absolute;left:0;top:0}
.env-one .brand{position:absolute;left:0;right:0;top:26px}
.env-two{top:307px;height:214px}
.env-two-head{height:60px;background:var(--ink);display:flex;align-items:center;justify-content:center}
.env-two .letterhead-foot{padding:0 14px 14px}
</style>
</head>
<body>

<div class="label" style="left:29px;top:240px">Stationery Concept</div>

<div class="piece card card-front">
  <div class="brand"><span class="brand-dot"></span><span class="brand-name">BRISKFIELD</span></div>
  <div class="card-person">Tomas Kerbrune</div>
  <div class="card-role">Director</div>
  <div class="card-contact">+33 612 48 90 27 · info@briskfield-exemple.com</div>
</div>
<div class="label" style="left:44px;top:361px">Business Card Front</div>

<div class="piece card card-back">
  <div class="brand"><span class="brand-dot"></span><span class="brand-name">BRISKFIELD</span></div>
  <div class="card-contact">www.briskfield-exemple.com</div>
</div>
<div class="label" style="left:46px;top:488px">Business Card Back</div>

<div class="piece letterhead">
  <div class="letterhead-head">
    <div class="brand"><span class="brand-dot"></span><span class="brand-name">BRISKFIELD</span></div>
  </div>
  <div class="rule"></div>
  <div class="watermark"><span>BRISKFIELD</span></div>
  <div class="letterhead-foot">
    <div class="rule"></div>
    <div class="foot-text"><span><i>●</i> +33 612 48 90 27</span><span><i>●</i> info@briskfield-exemple.com</span><span><i>●</i> www.briskfield-exemple.com</span></div>
  </div>
</div>
<div class="label" style="left:390px;top:578px">Letter Head Option 1</div>

<div class="piece envelope env-one">
  <svg width="452" height="211" viewBox="0 0 452 211">
    <path d="M0 0H452V62L226 108L0 62Z" fill="#161617"/>
    <path d="M0 62L226 108L452 62" fill="none" stroke="#d8372a" stroke-width="2"/>
  </svg>
  <div class="brand"><span class="brand-dot"></span><span class="brand-name">BRISKFIELD</span></div>
</div>

<div class="piece envelope env-two">
  <div class="env-two-head">
    <div class="brand"><span class="brand-dot"></span><span class="brand-name">BRISKFIELD</span></div>
  </div>
  <div class="rule"></div>
  <div class="letterhead-foot">
    <div class="rule"></div>
    <div class="foot-text"><span><i>●</i> +33 612 48 90 27</span><span><i>●</i> info@briskfield-exemple.com</span><span><i>●</i> www.briskfield-exemple.com</span></div>
  </div>
</div>
<div class="label" style="left:880px;top:528px">Envelope Option 2</div>

</body>
</html>
```